Facebook Post for Fence Spring Sale

We have a $12 / FT Fence sale that we have been running for a while now. We need a flyer made up for SPRING.

Our previous flyer can be seen here:
https://media.pixvault-host.example/img/48213907_551903288146720_7391026458813302947_n.jpg?ref=7c21b9e04d8a

We want to use the photos that are shown here https://files.cloudtrove-share.example/view?id=9XkQ7rTmw2LpZdVa4HsE in the flyer. This is to be posted on Facebook so it must be the proper size for Facebook page post.

The wording to be used should be "Spring Fence Sale" and "$12 / FT Wood Fences" Also we should include our business name "Oakridge Fence" and phone number for Free Estimates - 555-314-2076.

Residential Construction

Font styles to use
Serif
Sans Serif

Colors
3176b5
fbee3d
fbed22
fbf289
85cae6
33a6d7

Requirements
Must have
• Phone number, $12 / FT Fence Sale

```html
<!DOCTYPE html>
<html lang="en">
<head>
<meta charset="utf-8">
<title>Oakridge Fence – Spring Fence Sale</title>
<link rel="stylesheet" href="https://fonts.googleapis.com/css2?family=Roboto:ital,wght@0,400;0,700;0,900;1,400;1,500&family=Playfair+Display:ital,wght@1,700&family=Roboto+Slab:wght@800&display=swap">
<style>
  :root {
    --page-bg: #e9eef3;
    --brand-blue: #2a6fae;
    --deep-blue: #3176b5;
    --sky-blue: #85cae6;
    --light-blue: #b4e2f7;
    --mid-blue: #33a6d7;
    --yellow: #fbee22;
    --pale-yellow: #fbf289;
    --cream: #fff8e6;
    --white: #ffffff;
    --ink: #111111;
    --petal-border: #fbf5e6;
  }
  * { margin: 0; padding: 0; box-sizing: border-box; }
  html, body { width: 1200px; height: 1000px; overflow: hidden; background: var(--page-bg); }
  .canvas { position: relative; width: 1200px; height: 1000px; }
  .post {
    position: absolute; left: 205px; top: 105px; width: 790px; height: 790px;
    overflow: hidden; background: var(--white);
    font-family: "Roboto", Arial, sans-serif;
  }
  .post-bg { position: absolute; inset: 0; }
  .floral { position: absolute; }
  .floral-top-left { left: 0; top: 0; width: 300px; height: 150px; opacity: .8;
    background: radial-gradient(ellipse at 45% 35%, rgba(245,180,200,.9), rgba(250,230,120,.5) 40%, rgba(255,255,255,0) 70%); }
  .floral-side-left { left: 0; top: 100px; width: 110px; height: 200px; opacity: .8;
    background: radial-gradient(ellipse at 20% 50%, rgba(240,150,90,.8), rgba(120,190,150,.45) 45%, rgba(133,202,230,0) 72%); }
  .floral-top-right { left: 430px; top: 0; width: 360px; height: 280px;
    background: radial-gradient(ellipse at 60% 20%, rgba(240,150,190,.85), rgba(120,180,120,.4) 45%, rgba(255,255,255,0) 72%); }
  .floral-bottom-right { left: 725px; top: 710px; width: 65px; height: 80px;
    background: radial-gradient(circle at 60% 60%, rgba(240,160,90,.8), rgba(120,190,150,.5) 50%, rgba(42,111,174,0) 75%); }

  .brand { position: absolute; left: 185px; top: 140px; width: 120px; text-align: center; }
  .brand-mark { display: block; width: 22px; height: 22px; margin: 0 auto 10px; background: #7a5530; }
  .brand-name { font-size: 12px; font-weight: 400; color: var(--deep-blue); }
  .brand-tagline { font-size: 5px; color: var(--ink); margin-top: 3px; white-space: nowrap; }

  .petal {
    position: absolute; border: 6px solid var(--petal-border);
    box-shadow: 0 2px 6px rgba(0,0,0,.25);
  }
  .petal-tl { left: 302px; top: 64px; width: 204px; height: 196px; border-radius: 110px 14px 0 110px;
    background: linear-gradient(160deg, #d8cfa6, #6e8a3c 60%, #3f5a22); }
  .petal-tr { left: 518px; top: 64px; width: 200px; height: 196px; border-radius: 14px 110px 110px 0;
    background: linear-gradient(200deg, #7fa34a, #c9b07a 55%, #6f8d3a); }
  .petal-bl { left: 302px; top: 272px; width: 204px; height: 198px; border-radius: 110px 0 14px 110px;
    background: linear-gradient(120deg, #c4a880, #e6d3ae 50%, #a98b62); }
  .petal-br { left: 518px; top: 272px; width: 274px; height: 276px; border-radius: 0 14px 140px 140px;
    background: linear-gradient(100deg, #b08c5c, #e9d3a6 55%, #8aa25a); }

  .headline-spring {
    position: absolute; left: 73px; top: 248px; line-height: 70px;
    font-family: "Playfair Display", Georgia, serif; font-style: italic; font-weight: 700;
    font-size: 64px; color: var(--white);
    text-shadow: 2px 3px 4px rgba(0,0,0,.35);
  }
  .headline-line {
    position: absolute; left: 50px; font-weight: 700; font-size: 80px; line-height: 70px;
    color: var(--light-blue); letter-spacing: -2px; text-shadow: 2px 3px 4px rgba(0,0,0,.3);
  }
  .headline-fence { top: 318px; }
  .headline-sale { top: 388px; }

  .price-amount {
    position: absolute; left: 50px; top: 478px;
    font-weight: 900; font-size: 150px; line-height: 130px; color: var(--yellow);
    letter-spacing: -6px; text-shadow: 2px 3px 3px rgba(0,0,0,.35);
  }
  .price-unit {
    position: absolute; left: 161px; top: 604px; background: var(--ink); color: var(--yellow);
    font-style: italic; font-size: 22px; line-height: 26px; padding: 0 6px; white-space: nowrap;
  }
  .product {
    position: absolute; left: 27px; top: 648px; width: 285px; text-align: center;
    font-family: "Roboto Slab", Georgia, serif; font-weight: 800; font-size: 58px; line-height: 58px;
    color: var(--cream); text-shadow: 2px 3px 3px rgba(0,0,0,.5);
  }

  .estimate { position: absolute; left: 340px; top: 560px; width: 420px; text-align: center; }
  .estimate-label { font-style: italic; font-size: 26px; color: var(--white); margin-left: 60px; }
  .estimate-phone {
    font-weight: 900; font-size: 45px; color: var(--yellow); margin-top: 6px;
    text-shadow: 2px 3px 3px rgba(0,0,0,.4);
  }
  .chevron { position: absolute; left: 527px; top: 680px; }
  .website { position: absolute; left: 340px; top: 722px; width: 420px; text-align: center; color: var(--white); }
  .website-label { font-style: italic; font-size: 15px; }
  .website-url { font-weight: 700; font-size: 18px; margin-top: 6px; }
</style>
</head>
<body>
<div class="canvas">
  <div class="post">
    <svg class="post-bg" width="790" height="790" viewBox="0 0 790 790">
      <path d="M0 40 C90 150 250 200 430 250 L620 290 L790 300 L790 790 L0 790 Z" fill="#85cae6"/>
      <path d="M0 150 C110 220 260 250 420 275 L600 300 L790 310 L790 790 L0 790 Z" fill="#2a6fae"/>
      <ellipse cx="545" cy="620" rx="220" ry="70" fill="#85cae6" opacity=".28"/>
      <ellipse cx="545" cy="790" rx="215" ry="95" fill="#85cae6" opacity=".32"/>
    </svg>

    <div class="floral floral-top-left" role="img" aria-label="Watercolour spring flowers and leaves"></div>
    <div class="floral floral-side-left" role="img" aria-label="Watercolour flower cluster along the edge"></div>
    <div class="floral floral-top-right" role="img" aria-label="Watercolour pink blossoms with green leaves"></div>
    <div class="floral floral-bottom-right" role="img" aria-label="Small watercolour flower cluster"></div>

    <div class="brand">
      <span class="brand-mark"></span>
      <div class="brand-name">Oakridge Fence</div>
      <div class="brand-tagline">"Because Good Fences Make Good Neighbors"</div>
    </div>

    <div class="petal petal-tl" role="img" aria-label="Photo of a split rail wood fence on a lawn"></div>
    <div class="petal petal-tr" role="img" aria-label="Photo of a spaced picket wood fence with rails"></div>
    <div class="petal petal-bl" role="img" aria-label="Photo of a wooden picket gate with black hinges"></div>
    <div class="petal petal-br" role="img" aria-label="Photo of a new wood privacy fence along a yard"></div>

    <div class="headline-spring">Spring</div>
    <div class="headline-line headline-fence">Fence</div>
    <div class="headline-line headline-sale">Sale!</div>

    <div class="price-amount">$12</div>
    <div class="price-unit">PER FEET</div>
    <div class="product">WOOD<br>FENCES</div>

    <div class="estimate">
      <div class="estimate-label">Free Estimates</div>
      <div class="estimate-phone">555-314-2076</div>
    </div>
    <svg class="chevron" width="38" height="26" viewBox="0 0 38 26">
      <polyline points="2,2 19,14 36,2" fill="none" stroke="#ffffff" stroke-width="2"/>
      <polyline points="2,11 19,23 36,11" fill="none" stroke="#ffffff" stroke-width="2"/>
    </svg>
    <div class="website">
      <div class="website-label">For more information, Visit:</div>
      <div class="website-url">myoakridgefence.example</div>
    </div>
  </div>
</div>
</body>
</html>
```